BLQ Business Card

We need a business card that reflect our business, we have put anther business card as an example of what we like but please feel free to do your own thing.

Here are the items to be placed on card

Wade Pelham
Amber Harbor Supply
Mobile: 917-555-4820
Office: 516-555-7164
Fax: 866-555-3291
Email: info@amberharborsupply-example.com
Website: amberharborsupply-example.com

I have added raw files to upload

Wade Pelham
Amber Harbor Supply
Mobile: 917-555-4820
Office: 516-555-7164
Fax: 866-555-3291 

Target Market(s)

Natural product manufactures, and retailers and distributors

Industry/Entity Type

Business

Requirements
Must have
• 1. Logo
2. The colors of the company

```html
<!DOCTYPE html>
<html lang="en">
<head>
<meta charset="utf-8">
<title>Amber Harbor Supply – Business Card</title>
<link rel="stylesheet" href="https://fonts.googleapis.com/css2?family=Exo+2:wght@300;400;600;800&display=swap">
<style>
  :root {
    --page-bg: #e6e4e0;
    --card-white: #f7f7f7;
    --card-white-edge: #e2e2e2;
    --panel-dark: #2a2a2a;
    --panel-mid: #5e5e5e;
    --ink-light: #ffffff;
    --ink-grey: #5a5a5a;
    --brand-green: #7dbb1f;
  }
  * { margin: 0; padding: 0; box-sizing: border-box; }
  html, body {
    width: 1200px; height: 1085px; overflow: hidden;
    background: var(--page-bg);
    font-family: "Exo 2", sans-serif;
  }
  .business-card {
    position: absolute; left: 100px; top: 256px;
    width: 1000px; height: 572px;
    background: linear-gradient(135deg, var(--card-white) 40%, var(--card-white-edge));
    box-shadow: 0 18px 40px rgba(0,0,0,.22);
    overflow: hidden;
  }
  .contact-panel { position: absolute; inset: 0; }
  .contact-row {
    position: absolute; right: 555px;
    color: var(--ink-light); text-align: right;
    font-size: 24px; font-weight: 400; line-height: 1.3; letter-spacing: .5px;
  }
  .contact-row--phone { top: 116px; }
  .contact-row--address { top: 233px; }
  .contact-row--web { top: 392px; font-size: 20px; }
  .brand-name {
    position: absolute; left: 590px; top: 70px;
    color: var(--brand-green);
    font-weight: 800; font-size: 44px; line-height: 1.02;
    text-transform: uppercase; letter-spacing: 1px;
  }
  .holder { position: absolute; left: 590px; top: 330px; }
  .holder-name {
    color: var(--ink-grey); font-weight: 300;
    font-size: 40px; letter-spacing: 3px; text-transform: uppercase;
  }
  .holder-title {
    color: var(--brand-green); font-weight: 400;
    font-size: 27px; letter-spacing: 1px; margin-top: 4px;
  }
</style>
</head>
<body>
  <div class="business-card">
    <svg class="contact-panel" width="1000" height="572" viewBox="0 0 1000 572" aria-hidden="true">
      <defs>
        <linearGradient id="panelShade" x1="0" y1="0" x2="1" y2="1">
          <stop offset="0" stop-color="var(--panel-dark)"/>
          <stop offset="1" stop-color="var(--panel-mid)"/>
        </linearGradient>
      </defs>
      <path fill="url(#panelShade)" d="M0 0 H480 V92 C480 112 530 106 530 150 C530 194 480 188 480 208 V228 C480 248 530 242 530 286 C530 330 480 324 480 344 V364 C480 384 530 378 530 422 C530 466 480 460 480 480 V572 H0 Z"/>
      <g fill="none" stroke="#fff" stroke-width="3">
        <circle cx="500" cy="150" r="23"/>
        <circle cx="500" cy="286" r="23"/>
        <circle cx="500" cy="422" r="23"/>
      </g>
      <!-- phone -->
      <path fill="#fff" d="M491 139 c3-2 5-1 6 1 l2 5 c1 2 0 3-2 4 c1 4 4 7 8 8 c1-2 2-3 4-2 l5 2 c2 1 3 3 1 6 c-2 3-5 4-9 2 c-8-3-14-9-17-17 c-1-4 0-7 2-9 z"/>
      <!-- pin -->
      <path fill="#fff" d="M500 272 c-7 0-12 5-12 12 c0 8 12 19 12 19 s12-11 12-19 c0-7-5-12-12-12 z"/>
      <circle cx="500" cy="284" r="4.5" fill="var(--panel-mid)"/>
      <!-- globe -->
      <g fill="none" stroke="#fff" stroke-width="2">
        <circle cx="500" cy="422" r="13"/>
        <ellipse cx="500" cy="422" rx="6" ry="13"/>
        <line x1="487" y1="422" x2="513" y2="422"/>
        <line x1="489" y1="415" x2="511" y2="415"/>
        <line x1="489" y1="429" x2="511" y2="429"/>
      </g>
    </svg>

    <div class="contact-row contact-row--phone">917-555-4820<br>516-555-7164</div>
    <div class="contact-row contact-row--address">214 Harbor Row, 6th floor,<br>Dock Street<br>NJ</div>
    <div class="contact-row contact-row--web">info@amberharborsupply-example.com<br>amberharborsupply-example.com</div>

    <div class="brand-name">Amber Harbor<br>Supply</div>

    <div class="holder">
      <div class="holder-name">Wade Pelham</div>
      <div class="holder-title">Managing Director</div>
    </div>
  </div>
</body>
</html>
```